Varlow's Electrical & Solar - Business Cards

I want my business card to stand out from the rest. I will provide my business name logo and my icon logo to be implemented onto the card.

On the front of the card, can i have the following. Just make it neat & professional please.

Dean Harrop
varlowselectrical@mailbox-example.net
0491 837 562
ABN: 41 269 507 813
License No. 582146K
FREE QUOTES
24/7 Emergency

On the back of the card, can I have "Our Services" and maybe add the V logo on the back in the background or something. Under "Our Services" I want the following:

LED Lighting Upgrades
Switches & Outlets
Smoke Alarms
Switchboard Upgrades
Fault Finding
Rewiring
New Builds
Test & Tagging
All Electrical Maintenance & Repairs

Can you guys add the instagram logo and next to it, put varlows_electrical

Can you guys also add the facebook logo and next to it put Varlow's Electrical & Solar. Make sure the instagram & facebook icon is in either white, green or black.

Also I have put down double sided, not sure why when i save it, it keeps going to single sided. I need my business card double sided.

New Customers

Dean Harrop varlowselectrical@mailbox-example.net 0491 837 562 ABN: 41 269 507 813 License No. 582146K FREE QUOTES 24/7 Emergency

• must be tidy, professional and appealing

```html
<!DOCTYPE html>
<html lang="en">
<head>
<meta charset="utf-8">
<title>Varlow's Electrical &amp; Solar – Business Cards</title>
<link rel="stylesheet" href="https://fonts.googleapis.com/css2?family=Poppins:wght@400;500;600;700&family=Russo+One&display=swap">
<style>
  :root {
    --backdrop: #2a2a2c;
    --card: #1e1f21;
    --card-back: #141415;
    --green: #2fc23d;
    --text: #e4e4e4;
    --muted: #a9a9a9;
    --rule: #d8d8d8;
  }
  * { box-sizing: border-box; margin: 0; padding: 0; }
  html, body { width: 1200px; height: 1108px; overflow: hidden; }
  body {
    background: var(--backdrop);
    font-family: "Poppins", sans-serif;
    color: var(--text);
    position: relative;
  }
  .card {
    position: absolute;
    top: 164px;
    width: 500px;
    height: 780px;
    border-radius: 30px;
    overflow: hidden;
  }
  .card--front { left: 70px; background: var(--card); text-align: center; }
  .card--back { left: 630px; background: var(--card-back); }

  .brand { margin-top: 84px; display: flex; flex-direction: column; align-items: center; }
  .brand__mark {
    width: 92px; height: 92px; border-radius: 50%;
    border: 8px solid var(--green);
  }
  .brand__name {
    margin-top: 18px;
    font-weight: 700; font-size: 52px; letter-spacing: 1px;
    color: var(--text); line-height: 1;
  }
  .brand__tag {
    margin-top: 8px; font-size: 13px; letter-spacing: 6px;
    color: var(--muted); text-transform: uppercase;
  }

  .person {
    margin-top: 40px;
    font-family: "Russo One", sans-serif;
    font-weight: 400;
    font-size: 30px; color: var(--green); letter-spacing: 1px;
  }

  .divider { display: flex; align-items: center; justify-content: center; gap: 8px; margin: 14px auto 10px; width: 300px; }
  .divider__line { flex: 1; height: 1px; background: var(--rule); }
  .divider__icon {
    width: 28px; height: 28px; border-radius: 50%;
    border: 1.5px solid var(--green);
    display: flex; align-items: center; justify-content: center;
  }
  .divider__icon svg { width: 14px; height: 14px; }
  .rule { width: 300px; height: 1px; background: var(--rule); margin: 14px auto; }

  .contact { font-size: 22px; line-height: 1.35; }
  .contact--email { font-size: 19px; white-space: nowrap; }
  .label { color: var(--green); }

  .cta { margin-top: 18px; font-size: 22px; letter-spacing: .5px; }
  .cta__sep { margin: 0 10px; }
  .cta__urgent { color: var(--green); font-weight: 600; }

  .back__pattern {
    position: absolute; inset: 0;
    background: radial-gradient(circle at 80% 15%, #4a4a4d 0%, #262628 40%, #0f0f10 80%);
  }
  .services {
    position: absolute; left: 0; right: 0; top: 330px;
    text-align: center;
  }
  .services__title {
    font-family: "Russo One", sans-serif;
    font-weight: 400;
    color: var(--green); font-size: 34px; margin-bottom: 18px; letter-spacing: 1px;
  }
  .services__list { list-style: none; font-size: 20px; line-height: 1.5; text-transform: uppercase; color: #f2f2f2; }
</style>
</head>
<body>

  <section class="card card--front" aria-label="Front of business card">
    <div class="brand">
      <div class="brand__mark"></div>
      <div class="brand__name">VARLOW'S</div>
      <div class="brand__tag">Electrical &amp; Solar</div>
    </div>

    <h1 class="person">DEAN HARROP</h1>

    <div class="divider">
      <span class="divider__line"></span>
      <span class="divider__icon">
        <svg viewBox="0 0 24 24" fill="none" stroke="#2fc23d" stroke-width="2"><path d="M5 3h4l2 5-3 2a11 11 0 0 0 6 6l2-3 5 2v4a2 2 0 0 1-2 2A17 17 0 0 1 3 5a2 2 0 0 1 2-2z"/></svg>
      </span>
      <span class="divider__icon">
        <svg viewBox="0 0 24 24" fill="none" stroke="#2fc23d" stroke-width="2"><rect x="3" y="5" width="18" height="14" rx="2"/><path d="M3 7l9 6 9-6"/></svg>
      </span>
      <span class="divider__line"></span>
    </div>

    <p class="contact">0491 837 562</p>
    <p class="contact contact--email">varlowselectrical@mailbox-example.net</p>

    <div class="rule"></div>

    <p class="contact"><span class="label">ABN:</span> 41 269 507 813</p>
    <p class="contact"><span class="label">License No.</span> 582146K</p>

    <div class="divider">
      <span class="divider__line"></span>
      <span class="divider__icon" aria-label="Social handle"></span>
      <span class="divider__icon" aria-label="Social page"></span>
      <span class="divider__line"></span>
    </div>

    <p class="contact">varlows_electrical</p>
    <p class="contact">Varlow's Electrical &amp; Solar</p>

    <div class="rule"></div>

    <p class="cta">FREE QUOTES<span class="cta__sep">|</span><span class="cta__urgent">24/7 EMERGENCY</span></p>
  </section>

  <section class="card card--back" aria-label="Back of business card">
    <div class="back__pattern" role="img" aria-label="Repeating glossy V logo pattern in dark greys"></div>
    <div class="services">
      <h2 class="services__title">OUR SERVICES</h2>
      <ul class="services__list">
        <li>LED Lighting Upgrades</li>
        <li>Switches &amp; Outlets</li>
        <li>Smoke Alarms</li>
        <li>Switchboard Upgrades</li>
        <li>Fault Finding</li>
        <li>Rewiring</li>
        <li>New Builds</li>
        <li>Test &amp; Tagging</li>
        <li>All Electrical Maintenance<br>&amp; Repairs</li>
      </ul>
    </div>
  </section>

</body>
</html>
```